Silverleaf Rise Accounting Program

size of ad Full: 7” x 9.6”
1- this is for a ladies program so it should appeal to women.
2-however, I do not want any pictures of people in this ad.
3-all the text should be seen and not covered over by graphics.
4-It should be an ad that will draw people's attention and people should look at it and say it looks nice I want to see that ad.
5-I have put all the instructions in yellow in the file below.
6-please leave 1 inch for the footer .
good luck with this project

• no picture or vector of people.

```html
<!DOCTYPE html>
<html lang="en">
<head>
<meta charset="utf-8">
<title>Prime Masters &amp; MBA Ranking 2019 – Accounting Open House</title>
<link rel="stylesheet" href="https://fonts.googleapis.com/css2?family=Montserrat:wght@600;700&family=Ubuntu:wght@400;500;700&display=swap">
<style>
  :root {
    --orange: #e8750f;
    --ink: #2b2b2b;
    --text: #333333;
    --panel: #e2e2e2;
    --paper: #ffffff;
    --pattern-a: #fdf3ea;
    --pattern-b: #ffffff;
    --rule: #4a4a4a;
  }
  html, body {
    margin: 0;
    padding: 0;
    width: 745px;
    height: 1200px;
    overflow: hidden;
    background: var(--paper);
  }
  .flyer {
    position: relative;
    width: 745px;
    height: 1200px;
    background: var(--paper);
    font-family: "Ubuntu", sans-serif;
    color: var(--text);
    text-align: center;
  }
  .flyer__pattern {
    position: absolute;
    inset: 0;
    background: linear-gradient(135deg, var(--pattern-a) 0%, var(--pattern-b) 45%, var(--pattern-a) 100%);
  }
  .flyer__frame {
    position: absolute;
    left: 31px; right: 31px; top: 30px; bottom: 26px;
    border: 2px solid var(--orange);
  }
  .block {
    position: absolute;
    left: 0; right: 0;
    margin: 0;
  }
  .brand { top: 52px; }
  .brand__mark {
    display: block;
    width: 86px; height: 86px;
    margin: 0 auto 12px;
    border-radius: 50%;
    background: var(--orange);
  }
  .brand__name {
    font-family: "Montserrat", sans-serif;
    font-weight: 600;
    font-size: 19px;
    color: var(--orange);
    letter-spacing: 0.5px;
  }
  .headline__kicker {
    top: 253px;
    font-family: "Montserrat", sans-serif;
    font-weight: 700;
    font-size: 24px;
    color: var(--ink);
    letter-spacing: 0.5px;
  }
  .headline__main {
    top: 289px;
    font-family: "Montserrat", sans-serif;
    font-weight: 700;
    font-size: 55px;
    line-height: 1;
    color: var(--orange);
    letter-spacing: 1px;
  }
  .headline__year {
    top: 352px;
    font-family: "Montserrat", sans-serif;
    font-weight: 700;
    font-size: 126px;
    line-height: 1;
    color: var(--orange);
  }
  .divider {
    position: absolute;
    top: 500px;
    left: 50%;
    width: 96px;
    margin-left: -48px;
    height: 3px;
    background: var(--rule);
  }
  .section-title {
    font-family: "Ubuntu", sans-serif;
    font-weight: 500;
    font-size: 23px;
    color: var(--orange);
    letter-spacing: 0.3px;
  }
  .degree__title { top: 522px; }
  .degree__text { top: 560px; font-size: 16px; line-height: 21px; }
  .advantage__title { top: 620px; }
  .advantage__panel {
    position: absolute;
    top: 660px;
    left: 103px; right: 103px;
    height: 72px;
    background: var(--panel);
    display: flex;
    align-items: center;
    justify-content: center;
    font-size: 16px;
    font-weight: 500;
    line-height: 21px;
    color: var(--ink);
  }
  .placement { top: 764px; font-size: 18px; line-height: 23px; font-weight: 500; }
  .open-house__button {
    position: absolute;
    top: 826px;
    left: 50%;
    width: 254px;
    margin-left: -127px;
    height: 42px;
    line-height: 42px;
    background: var(--orange);
    color: var(--paper);
    font-size: 21px;
    font-weight: 500;
    letter-spacing: 0.3px;
  }
  .open-house__details {
    top: 882px;
    font-size: 18px;
    line-height: 23px;
    font-weight: 500;
    color: var(--ink);
  }
  .accreditation { top: 970px; font-size: 15px; line-height: 19px; }
  .program-length { top: 1022px; font-size: 15px; }
  .website {
    top: 1060px;
    font-size: 17px;
    font-weight: 500;
    color: var(--ink);
  }
  .website__name { color: var(--orange); }
</style>
</head>
<body>
  <main class="flyer">
    <div class="flyer__pattern" role="img" aria-label="Soft cream diagonal chevron background pattern"></div>
    <div class="flyer__frame"></div>

    <div class="block brand">
      <span class="brand__mark"></span>
      <div class="brand__name">Prime Masters</div>
    </div>

    <h2 class="block headline__kicker">PRIME MASTERS &amp; MBA RANKING</h2>
    <h1 class="block headline__main">WORLDWIDE</h1>
    <div class="block headline__year">2019</div>
    <div class="divider"></div>

    <h3 class="block section-title degree__title">A Master’s Degree in Accounting</h3>
    <p class="block degree__text">A stable, lucrative career, with high-paying, full /part time<br>opportunities in Private/Public companies</p>

    <h3 class="block section-title advantage__title">The Ridgeway Job Placement advantage</h3>
    <div class="advantage__panel">96% Placement Rate - &nbsp; 6 placement directors - decades of<br>relationships with 100’s of firms</div>

    <p class="block placement">Graduates have been placed in top companies<br>(full/part time jobs).</p>

    <div class="open-house__button">Meetly open house</div>
    <p class="block open-house__details">Sunday June 14,2pm<br>for a Meetly &nbsp;link / conference number /information<br>info@ridgewayjobs.org &nbsp;or 555 014 2700x 111</p>

    <p class="block accreditation">Harrow Vale University, Masters in Accounting program,<br>received the highest possible rating in USA</p>
    <p class="block program-length">Masters in 12</p>
    <p class="block website">www.<span class="website__name">prime-masters</span>.org</p>
  </main>
</body>
</html>
```